Kelvo Marine business card

We sell live saltwater fish and live corals
Kelvo Marine
7 Harlow Ct
Corwin, ST. 00421
(555) 555-0147
Contact Information for Business Card
Kelvo Marine
7 Harlow Ct
Corwin, ST. 00421
(555) 555-0147
Colors
Designer to choose colors to be used in the design.

```html
<!DOCTYPE html>
<html lang="en">
<head>
<meta charset="utf-8">
<title>Kelvo Marine Business Card</title>
<link rel="stylesheet" href="https://fonts.googleapis.com/css2?family=Montserrat:wght@600&family=Roboto:wght@400;500&display=swap">
<style>
  :root {
    --backdrop: #161616;
    --paper: #f3f3f2;
    --deep-teal: #235c71;
    --brand-teal: #1f5a6e;
    --aqua: #3cb6c7;
    --ink-light: #f2f6f8;
  }
  html, body {
    margin: 0;
    padding: 0;
    width: 1200px;
    height: 1138px;
    overflow: hidden;
    background: var(--backdrop);
  }
  .card {
    position: absolute;
    left: 100px;
    top: 266px;
    width: 1000px;
    height: 605px;
    border-radius: 20px;
    overflow: hidden;
    background: var(--paper);
  }
  .card-shapes {
    position: absolute;
    inset: 0;
    width: 1000px;
    height: 605px;
  }
  .brand-block {
    position: absolute;
    left: 0;
    top: 122px;
    width: 500px;
    display: flex;
    flex-direction: column;
    align-items: center;
    gap: 66px;
  }
  .brand-dot {
    width: 180px;
    height: 180px;
    border-radius: 50%;
    background: var(--brand-teal);
  }
  .brand-name {
    margin: 0;
    font-family: "Montserrat", sans-serif;
    font-weight: 600;
    font-size: 44px;
    line-height: 54px;
    letter-spacing: 0.5px;
    color: var(--brand-teal);
  }
  .contact-block {
    position: absolute;
    left: 584px;
    top: 170px;
    font-family: "Roboto", sans-serif;
  }
  .company-title {
    margin: 0 0 93px;
    font-weight: 500;
    font-size: 34px;
    color: var(--aqua);
  }
  .contact-list {
    list-style: none;
    margin: 0;
    padding: 0;
    font-size: 28px;
    font-weight: 400;
    color: var(--ink-light);
    line-height: 43px;
  }
  .contact-list li {
    display: flex;
    align-items: center;
  }
  .contact-icon {
    width: 28px;
    height: 28px;
    margin-right: 30px;
    flex: none;
  }
  .icon-spacer {
    width: 28px;
    margin-right: 30px;
    flex: none;
  }
</style>
</head>
<body>
  <div class="card">
    <svg class="card-shapes" viewBox="0 0 1000 605" aria-hidden="true">
      <path d="M410,0 Q596,302 410,605 L1000,605 L1000,0 Z" fill="var(--aqua)"/>
      <path d="M410,0 Q606,302 439,605 L1000,605 L1000,0 Z" fill="var(--deep-teal)"/>
    </svg>

    <div class="brand-block">
      <div class="brand-dot"></div>
      <p class="brand-name">Kelvo Marine</p>
    </div>

    <div class="contact-block">
      <h1 class="company-title">Kelvo Marine</h1>
      <ul class="contact-list">
        <li>
          <svg class="contact-icon" viewBox="0 0 24 24" aria-hidden="true">
            <path d="M3 9c0-3 4-4.5 9-4.5S21 6 21 9v1.5h-4.5V8.5h-9v2H3z" fill="var(--aqua)"/>
            <path d="M7 11h10l2 8H5z" fill="var(--aqua)"/>
            <circle cx="12" cy="15" r="2" fill="var(--deep-teal)"/>
          </svg>
          <span>(555) 555-0147</span>
        </li>
        <li>
          <svg class="contact-icon" viewBox="0 0 24 24" aria-hidden="true">
            <rect x="2" y="5" width="20" height="14" fill="var(--aqua)"/>
            <path d="M2 5l10 8 10-8M2 19l7.5-7M22 19l-7.5-7" fill="none" stroke="var(--deep-teal)" stroke-width="1.5"/>
          </svg>
          <span>7 Harlow Ct</span>
        </li>
        <li>
          <span class="icon-spacer"></span>
          <span>Corwin, ST. 00421</span>
        </li>
      </ul>
    </div>
  </div>
</body>
</html>
```